Launching a consulting business

I need a business card to launch a new consulting business. I provide executive level consultation throughout New York state to CEO and ED's who run and manage non-fo-profit corporations who support individuals with intellectual and developmental disabilities. The field is undergoing an evolution from a social model of care to more outcome based strategies. Having expertise in health care, leading a $50M business providing this service and working in the government creating policy I can bring to the Executive and corporations compassion, vision, strategy with a clear understanding of business practices for success. The field is moving to managed care. My background in health care management brings the expertise to create opportunities and possibilities. I currently have three projects I am consulting on - 1. Field expert assisting an accounting firm in the creation of a managed care application to become a managed care company supporting the ID/DD field. I crafted the care management model 2. Strategizing on product line creation to assure an agency is ready with a compendium services supporting the ID/DD field. 3. Facilitating a financial model to assist in predicting costs to render services in ID/DD. Developing and overlaying outcome measures to position agencies for effective marketing.
Quality is my passion and assuring all people live their life's dreams.
I would also like a template for letterhead stationary following what is created with my business card.
I wold like to incorporate a cranberry/sage tartan plaid within the design.

Please note my last name is spelled wrong on the attachment. I also do not want the tartan plaid used covering the entire card. i open to other ideas and suggestions.

Industry/Entity Type

Government

Contact Information for Business Card

Donna M Farris
Phone - 845-620-4178
Cell phone 845-733-2906
Email address - donnamfar@quillmail.com

```html
<!DOCTYPE html>
<html lang="en">
<head>
<meta charset="utf-8">
<title>Donna M Farris — Stationery Set</title>
<link rel="stylesheet" href="https://fonts.googleapis.com/css2?family=Open+Sans:wght@400;600&display=swap">
<style>
  :root {
    --bg: #e8e5de;
    --paper: #ffffff;
    --edge: #d9d6d0;
    --coral: #ef6f6b;
    --teal: #5cbfb3;
    --plaid-teal: #3fb2a5;
    --plaid-sage: #8fa59b;
    --plaid-cranberry: #e0575a;
    --window: #f1f1f2;
    --label: #111111;
  }
  * { margin: 0; padding: 0; box-sizing: border-box; }
  html, body { width: 1200px; height: 1000px; overflow: hidden; }
  body {
    position: relative;
    background: var(--bg);
    font-family: "Open Sans", Arial, sans-serif;
  }
  .sheet {
    position: absolute;
    background: var(--paper);
    border: 1px solid var(--edge);
  }
  .plaid-band {
    position: absolute;
    top: 0; left: 0; bottom: 0;
    background: linear-gradient(90deg, var(--plaid-cranberry) 0%, var(--plaid-teal) 30%, var(--plaid-sage) 55%, var(--plaid-teal) 75%, var(--plaid-cranberry) 100%);
    opacity: 0.9;
  }
  .name {
    position: absolute;
    color: var(--coral);
    font-weight: 600;
    letter-spacing: 0.04em;
    white-space: nowrap;
    line-height: 1;
  }
  .title {
    position: absolute;
    color: var(--teal);
    font-weight: 400;
    letter-spacing: 0.04em;
    white-space: nowrap;
    line-height: 1;
  }
  .contact {
    position: absolute;
    color: var(--coral);
    white-space: nowrap;
    line-height: 1;
    letter-spacing: 0.03em;
  }
  .contact .kind { color: var(--teal); }

  /* Letterhead */
  .letterhead { left: 62px; top: 63px; width: 656px; height: 849px; }
  .letterhead .plaid-band { width: 66px; }
  .letterhead .name { left: 82px; top: 42px; font-size: 29px; }
  .letterhead .title { left: 82px; top: 77px; font-size: 13px; }
  .letterhead .contact { top: 813px; font-size: 14px; }

  /* Business card */
  .bizcard { left: 563px; top: 207px; width: 410px; height: 232px; }
  .bizcard .plaid-band { width: 78px; }
  .bizcard .name { left: 103px; top: 51px; font-size: 19px; }
  .bizcard .title { left: 103px; top: 75px; font-size: 9px; }
  .bizcard .contact-list { position: absolute; left: 103px; top: 151px; }
  .bizcard .contact-list .contact { position: static; display: block; font-size: 12px; font-weight: 600; margin-bottom: 3px; }
  .bizcard .contact-list .kind { font-weight: 400; }

  /* Envelope */
  .envelope { left: 192px; top: 498px; width: 801px; height: 335px; }
  .envelope .plaid-band { width: 66px; }
  .envelope .name { left: 82px; top: 42px; font-size: 28px; }
  .envelope .title { left: 82px; top: 76px; font-size: 13px; }
  .envelope .address-window {
    position: absolute; left: 84px; top: 178px; width: 322px; height: 96px;
    background: var(--window); border-radius: 10px;
  }
  .envelope .contact { top: 305px; font-size: 10px; }

  .piece-label {
    position: absolute;
    color: var(--label);
    font-size: 40px;
    font-weight: 400;
    letter-spacing: 0.06em;
    line-height: 1;
  }
</style>
</head>
<body>

  <section class="sheet letterhead">
    <div class="plaid-band" role="img" aria-label="Cranberry and sage tartan plaid band"></div>
    <h1 class="name">Donna M Farris</h1>
    <p class="title">Executive Business Strategy Consultant</p>
    <p class="contact" style="left:82px">845-620-4178 <span class="kind">(tel)</span></p>
    <p class="contact" style="left:241px">845-733-2906 <span class="kind">(cell)</span></p>
    <p class="contact" style="left:412px">donnamfar@quillmail.com <span class="kind">(email)</span></p>
  </section>

  <section class="sheet envelope">
    <div class="plaid-band" role="img" aria-label="Cranberry and sage tartan plaid band"></div>
    <h2 class="name">Donna M Farris</h2>
    <p class="title">Executive Business Strategy Consultant</p>
    <div class="address-window"></div>
    <p class="contact" style="left:82px">845-620-4178 <span class="kind">(tel)</span></p>
    <p class="contact" style="left:196px">845-733-2906 <span class="kind">(cell)</span></p>
    <p class="contact" style="left:317px">donnamfar@quillmail.com <span class="kind">(email)</span></p>
  </section>

  <section class="sheet bizcard">
    <div class="plaid-band" role="img" aria-label="Cranberry and sage tartan plaid band"></div>
    <h2 class="name">Donna M Farris</h2>
    <p class="title">Executive Business Strategy Consultant</p>
    <div class="contact-list">
      <p class="contact">845-620-4178 <span class="kind">(tel)</span></p>
      <p class="contact">845-733-2906 <span class="kind">(cell)</span></p>
      <p class="contact">donnamfar@quillmail.com <span class="kind">(email)</span></p>
    </div>
  </section>

  <p class="piece-label" style="left:725px; top:68px">letterhead</p>
  <p class="piece-label" style="left:983px; top:207px">bizcard</p>
  <p class="piece-label" style="left:1001px; top:488px">envelope</p>

</body>
</html>
```